Vent doux

Hello,
I’m a designer sunglasses reatail Store owner in Montreal, Quebec.

Looking for something modern, fresh with a trendy appeal.

Will send my logo.
Thank you.

Store

```html
<!DOCTYPE html>
<html lang="fr">
<head>
<meta charset="utf-8">
<title>Vent doux – carte professionnelle</title>
<link rel="stylesheet" href="https://fonts.googleapis.com/css2?family=Open+Sans:wght@400;600&display=swap">
<style>
  :root {
    --brand-red: #c4122f;
    --card-frost: #f4f4f5;
    --circle-frost: #fafafb;
    --ink-dark: #231f20;
    --ink-light: #ffffff;
    --page-bg: #e4e4e6;
  }
  html, body {
    margin: 0;
    width: 1200px;
    height: 900px;
    overflow: hidden;
    background: var(--page-bg);
    font-family: "Open Sans", Arial, sans-serif;
  }
  .card {
    position: absolute;
    left: 166px;
    top: 182px;
    width: 867px;
    height: 536px;
  }
  .card-shape {
    position: absolute;
    inset: 0;
    width: 867px;
    height: 536px;
  }
  .card-body { fill: var(--card-frost); }
  .card-band { fill: var(--brand-red); }
  .card-circle { fill: var(--circle-frost); stroke: var(--brand-red); stroke-width: 7; }

  .holder-name {
    position: absolute;
    left: 42px;
    top: 40px;
    margin: 0;
    font-size: 34px;
    font-weight: 400;
    color: var(--ink-light);
    line-height: 1.2;
  }
  .holder-title {
    position: absolute;
    left: 42px;
    top: 86px;
    margin: 0;
    font-size: 22px;
    font-weight: 400;
    color: var(--ink-light);
  }
  .brand-name {
    position: absolute;
    left: 42px;
    top: 240px;
    margin: 0;
    font-size: 44px;
    font-weight: 600;
    letter-spacing: 1px;
    color: var(--ink-dark);
    line-height: 1.2;
  }
  .brand-emblem {
    position: absolute;
    left: 362px;
    top: 228px;
    width: 480px;
    margin: 0;
    text-align: center;
    font-size: 66px;
    font-weight: 600;
    line-height: 80px;
    color: var(--brand-red);
  }
  .contact-list {
    position: absolute;
    left: 42px;
    top: 408px;
    margin: 0;
    padding: 0;
    list-style: none;
    color: var(--ink-light);
    font-size: 22px;
  }
  .contact-item {
    display: flex;
    align-items: center;
    height: 31px;
  }
  .contact-icon {
    width: 16px;
    height: 16px;
    margin-right: 14px;
    fill: var(--ink-light);
    flex: none;
  }
</style>
</head>
<body>
  <article class="card">
    <svg class="card-shape" viewBox="0 0 667 412" aria-hidden="true">
      <rect class="card-body" x="0" y="0" width="463" height="412"/>
      <rect class="card-band" x="0" y="0" width="463" height="116"/>
      <rect class="card-band" x="0" y="294" width="463" height="118"/>
      <circle class="card-circle" cx="463" cy="206" r="201"/>
    </svg>

    <h1 class="holder-name">Olivier Garneau</h1>
    <p class="holder-title">Directeur général</p>

    <p class="brand-name">Vent doux</p>

    <p class="brand-emblem">Vent doux</p>

    <ul class="contact-list">
      <li class="contact-item">
        <svg class="contact-icon" viewBox="0 0 16 16" aria-hidden="true"><path d="M3.6 1.2l2.3 2.6-1.3 1.8c.9 2 2.6 3.7 4.6 4.6l1.8-1.3 2.6 2.3-1.4 2.2C7 14.8 1.2 9 .4 3.6z"/></svg>
        514-555 018 372
      </li>
      <li class="contact-item">
        <svg class="contact-icon" viewBox="0 0 16 16" aria-hidden="true"><path d="M1 3h14v10H1z M2 4.2v.6l6 4 6-4v-.6z" fill-rule="evenodd"/></svg>
        bonjour@ventdoux.ca
      </li>
      <li class="contact-item">
        <svg class="contact-icon" viewBox="0 0 16 16" aria-hidden="true"><path d="M6.5 9.5l3-3" stroke="#fff" stroke-width="1.6" fill="none"/><path d="M7 4.5l1.8-1.8a2.6 2.6 0 0 1 3.7 3.7L10.7 8.2 M9 11.5l-1.8 1.8a2.6 2.6 0 0 1-3.7-3.7l1.8-1.8" stroke="#fff" stroke-width="1.6" fill="none"/></svg>
        www.ventdoux.ca
      </li>
    </ul>
  </article>
</body>
</html>
```